Health & Fitness Author & Public Speaker Needs Visually Stunning Web Design!

We've FINALLY got around to launching a website for Belinda Marchetti - Australian Food Coach and Health & Fitness Expert. The website is to promote her new healthy eating program - "Bright Plate Living".
For a compehensive outline of exactly what we are after, please see the following attached files:
(1) Web Layout (wireframe, content/copy, links to photos to use, sample page we love)
(2) Style Guide (these are the colours, and overall feel we want)
Photos that we'd like used (of Belinda, and food/meals) can be found at these URL's:
Profile: https://www.filecrate.example/sh/q4r8vpl2m7xz/K3tPzWq9Lm
PicVault: https://www.filecrate.example/sh/b7nwe3ju1kd5/9hFrTy2Qxa
HINT:
Before you do ANYTHING - check out this site as it is pretty much EXACTLY what we're after, but with our branding/colours/style: http://tessamorrow.example/
As we will need to revamp our existing Chatterbook page & other printed material, there may be the potential for further work for the successful designer in the future.
Thanks & Good Luck!
Donovan Pryle
Marketing & Business Development Manager
Bright Plate Living
Women, Ages 24 - 45, Interested in Healthly Eating & Fitness
Business

```html
<!DOCTYPE html>
<html lang="en">
<head>
<meta charset="utf-8">
<title>Bright Plate Living</title>
<link href="https://fonts.googleapis.com/css2?family=Ubuntu:wght@500;700&family=Source+Sans+3:wght@400;600;700&family=Roboto+Condensed:wght@400;700&family=Oswald:wght@500;600&family=Cormorant+SC:wght@600&display=swap" rel="stylesheet">
<style>
:root{
  --page:#e6e6e6;
  --panel:#f1f1f1;
  --white:#ffffff;
  --pink:#ee1652;
  --pink-soft:#fbc3d4;
  --crimson:#a80f3d;
  --purple:#9b2a98;
  --ink:#333333;
  --ink-soft:#555555;
  --rule:#cfcfcf;
  --grey-icon:#9a9a9a;
}
*{box-sizing:border-box;margin:0;padding:0}
html,body{width:926px;height:1200px;overflow:hidden;background:var(--page)}
body{position:relative;font-family:"Source Sans 3",sans-serif;color:var(--ink)}
.abs{position:absolute}

/* hero */
.hero{left:29px;top:0;width:868px;height:443px;
  background:linear-gradient(160deg,#c9d8b4 0%,#7f9a55 35%,#5c7a36 60%,#8fa464 100%)}
.hero-figure{left:390px;top:56px;width:480px;height:387px;
  background:radial-gradient(ellipse at 55% 55%,#9a8a80 0%,#6f6b63 45%,rgba(90,110,60,0) 75%)}
.site-header{left:29px;top:0;width:868px;height:56px;background:rgba(255,255,255,.78)}
.brand{left:97px;top:14px;font-family:"Ubuntu",sans-serif;font-weight:700;font-size:17px;color:var(--purple);letter-spacing:-.2px}
.nav{left:525px;top:19px;display:flex;gap:36px;font-weight:700;font-size:14px;color:#3a3a3a}
.nav .current{color:var(--purple)}
.headline{left:116px;top:153px;display:flex;flex-direction:column;align-items:flex-start;gap:4px}
.headline span{background:var(--purple);color:var(--white);font-family:"Roboto Condensed",sans-serif;font-weight:700;font-size:24px;line-height:26px;padding:1px 5px;letter-spacing:-.5px}
.with-badge{left:66px;top:270px;width:48px;height:48px;border-radius:50%;background:#c0143f;color:var(--white);font-family:"Cormorant SC",serif;font-size:17px;display:flex;align-items:center;justify-content:center}
.coach-name{left:118px;top:274px;font-family:"Cormorant SC",serif;font-weight:600;font-size:31px;line-height:36px;color:var(--pink);letter-spacing:.5px}
.coach-role{left:116px;top:309px;font-family:"Roboto Condensed",sans-serif;font-size:15.5px;color:var(--white)}

/* signup band */
.signup-band{left:29px;top:443px;width:868px;height:75px;background:var(--pink)}
.band-title{left:102px;top:458px;font-weight:700;font-size:13.5px;color:var(--white)}
.band-text{left:102px;top:479px;width:280px;font-size:10px;line-height:13px;color:var(--pink-soft);text-transform:uppercase}
.mail-icon{left:405px;top:469px}
.field{background:var(--white);border:1px solid #d6d6d6;font-size:9px;color:#555;padding:0 7px;display:flex;align-items:center;height:23px}
.btn{display:flex;align-items:center;justify-content:center;color:var(--white);font-weight:700;font-size:9px}

/* main */
.main{left:29px;top:518px;width:868px;height:622px;background:var(--panel)}
.post-title{left:102px;width:440px;font-family:"Ubuntu",sans-serif;font-weight:500;font-size:21.5px;line-height:25px;color:var(--purple)}
.post-meta{left:103px;font-size:8.5px;color:var(--ink-soft)}
.post-meta b{font-weight:400;color:var(--pink)}
.post-body{left:103px;width:428px;font-size:10.8px;line-height:13px;color:var(--ink-soft);text-align:justify}
.share-row{left:104px;display:flex;gap:5px;align-items:center}
.share-row span{height:16px;display:flex;align-items:center;padding:0 6px;font-size:8px;color:var(--white);border-radius:2px}
.s-blue{background:#4a6aa5}.s-sky{background:#3fa8dc}.s-grey{background:#dcdcdc;color:#555!important}.s-green{background:#2e8b3c}.s-light{background:#eeeeee;color:#3b5998!important}.s-count{background:#fff;border:1px solid #ddd;color:#555!important}
.divider{left:102px;width:424px;height:1px;background:var(--rule)}

/* sidebar */
.guide-ad{left:558px;top:547px;width:256px;height:214px;background:linear-gradient(180deg,#f7c9d8 0%,#f2a2b8 35%,#d9454a 70%,#b8352c 100%)}
.guide-big{left:582px;top:566px;font-size:31px;line-height:36px;color:var(--pink)}
.guide-sub{left:582px;top:602px;width:220px;font-family:"Cormorant SC",serif;font-weight:600;font-size:17px;line-height:19px;color:#5a1f55}
.guide-btn{left:583px;top:649px;width:92px;height:26px;background:var(--pink);font-size:12px}
.challenge-ad{left:558px;top:788px;width:256px;height:175px;background:#e9e9ec}
.challenge-photo{left:558px;top:788px;width:125px;height:175px;background:radial-gradient(circle at 60% 55%,#c86a3c 0%,#8c3aa6 45%,#5a1a7a 100%)}
.challenge-top{left:690px;top:818px;font-family:"Oswald",sans-serif;font-weight:600;font-size:26px;line-height:24px;color:var(--purple)}
.challenge-mid{left:690px;top:842px;font-family:"Oswald",sans-serif;font-weight:600;font-size:22px;line-height:24px;color:var(--pink)}
.challenge-tag{left:691px;top:869px;font-family:"Oswald",sans-serif;font-weight:500;font-size:11px;line-height:14px;color:#222}
.challenge-tag em{font-style:normal;font-size:15px}
.challenge-btn{left:694px;top:908px;width:103px;height:30px;background:var(--purple);font-size:13px}
.join-title{left:558px;top:990px;width:256px;text-align:center;font-family:"Ubuntu",sans-serif;font-weight:500;font-size:14.5px;color:var(--purple)}
.join-text{left:558px;top:1010px;width:256px;text-align:center;font-size:9.5px;line-height:14px;color:var(--ink)}
.join-text b{font-weight:400;color:var(--pink)}

/* footer */
.footer-links{left:102px;top:1150px;display:flex;gap:12px;font-weight:700;font-size:16px;color:var(--ink)}
.footer-links i{font-style:normal;color:var(--pink)}
.copyright{left:102px;top:1175px;font-weight:600;font-size:8.5px;color:var(--ink)}
.social{top:1155px;width:31px;height:31px;background:var(--grey-icon)}
</style>
</head>
<body>

<div class="abs hero" role="img" aria-label="Photo of the food coach sitting cross-legged on park grass with a water bottle and boxing gloves"></div>
<div class="abs hero-figure"></div>

<header class="abs site-header"></header>
<div class="abs brand">brightplate living</div>
<nav class="abs nav"><span class="current">HOME</span><span>ABOUT</span><span>THE PLAN</span><span>SHOP</span></nav>

<div class="abs headline">
  <span>GET SLIM</span>
  <span>BOOST ENERGY</span>
  <span>GUILT FREE</span>
  <span>WITH BRIGHT PLATE LIVING!</span>
</div>
<div class="abs with-badge">with</div>
<div class="abs coach-name">Belinda Marchetti</div>
<div class="abs coach-role">FOOD COACH AND HEALTH &amp; FITNESS EXPERT</div>

<section class="abs signup-band"></section>
<div class="abs band-title">Join the BRIGHT PLATE LIVING MOVEMENT!</div>
<div class="abs band-text">Get a weekly serving of inspiration &amp; advice that will change your life…bring it on!</div>
<svg class="abs mail-icon" width="25" height="25" viewBox="0 0 25 25">
  <circle cx="12.5" cy="12.5" r="12" fill="#f45a83"/>
  <rect x="6.5" y="8.5" width="12" height="8" fill="none" stroke="#fff" stroke-width="1.3"/>
  <path d="M6.5 8.5 L12.5 13 L18.5 8.5" fill="none" stroke="#fff" stroke-width="1.3"/>
</svg>
<div class="abs field" style="left:445px;top:470px;width:121px">Your Name</div>
<div class="abs field" style="left:572px;top:470px;width:121px">Your Email</div>
<div class="abs btn" style="left:702px;top:468px;width:111px;height:25px;background:var(--crimson)">HOOK ME UP</div>

<main class="abs main"></main>

<h2 class="abs post-title" style="top:543px">Integer placerat, tellus et blandit molestie, purus leo semper massa, scelerisque</h2>
<div class="abs post-meta" style="top:596px">11th January 2012 // by <b>Warren Tolley</b> // <b>7 comments</b></div>
<p class="abs post-body" style="top:620px">Lorem ipsum dolor sit amet, consectetur adipiscing elit. Donec at tortor eget lorem porta aliquam. Praesent eget dolor quam, sit amet porttitor tortor. Curabitur ut nisi felis. Donec sed justo neque. Integer placerat, tellus et blandit molestie, purus leo semper massa, scelerisque dictum purus enim nec est. Aenean in mi tortor. Fusce sed mi urna. Phasellus vitae risus id erat fermentum suscipit. Aliquam mattis, odio vel adipiscing tincidunt, orci augue tincidunt turpis, at dapibus quam elit vitae turpis. Maecenas egestas nibh est. Phasellus suscipit tincidunt ligula, sit amet tristique turpis.</p>
<div class="abs share-row" style="top:731px"><span class="s-blue">Share</span><span class="s-sky">Post</span><span class="s-grey">Email</span><span class="s-green">Share</span><span class="s-light">Like</span><span class="s-count">23</span><span class="s-count">+1</span></div>
<div class="abs divider" style="top:765px"></div>

<h2 class="abs post-title" style="top:782px">In hac habitasse platea dictumst. Duis a consequat nisl viverra facilis</h2>
<div class="abs post-meta" style="top:837px">11th January 2012 // by <b>Warren Tolley</b> // <b>7 comments</b></div>
<p class="abs post-body" style="top:862px">Nullam eleifend risus vitae massa tincidunt eu feugiat diam vestibulum. Cum sociis natoque penatibus et magnis dis parturient montes, nascetur ridiculus mus. Donec fringilla suscipit diam vel tempus. Cum sociis natoque penatibus et magnis dis parturient montes, nascetur ridiculus mus. Phasellus pellentesque scelerisque ante, nec pulvinar eros euismod eget. Nunc in ullamcorper nunc. Nulla euismod, nisl hendrerit convallis blandit, diam turpis lobortis nunc, vitae ultricies turpis lacus vel magna. Class aptent taciti sociosqu ad litora torquent per conubia nostra, per inceptos himenaeos. In hac habitasse platea dictumst. Sed placerat magna non enim blandit ac fermentum mauris elementum. Vivamus malesuada est a justo posuere lobortis. Nullam vel gravida mi. Etiam pellentesque, ligula nec iaculis bibendum, nunc neque euismod nulla, a molestie enim velit a libero.</p>
<p class="abs post-body" style="top:1008px">Phasellus viverra lorem vel magna eleifend venenatis. Integer convallis sapien at lorem ullamcorper sed viverra massa tempus. Quisque interdum magna vitae ipsum cursus porta. Nam eget pellentesque dolor. Pellentesque habitant morbi tristique senectus et netus et malesuada fames ac turpis egestas. Nullam eleifend risus vitae massa tincidunt eu feugiat diam vestibulum.</p>
<div class="abs share-row" style="top:1075px"><span class="s-blue">Share</span><span class="s-sky">Post</span><span class="s-grey">Email</span><span class="s-green">Share</span><span class="s-light">Like</span><span class="s-count">23</span><span class="s-count">+1</span></div>
<div class="abs divider" style="top:1107px"></div>

<aside>
  <div class="abs guide-ad" role="img" aria-label="Close-up photo of a fresh salad with tomato, onion and capsicum"></div>
  <div class="abs guide-big">The Ultimate</div>
  <div class="abs guide-sub">Bright Plate Living Guide</div>
  <div class="abs btn guide-btn">GET IT NOW!</div>

  <div class="abs challenge-ad"></div>
  <div class="abs challenge-photo" role="img" aria-label="Photo of a salmon and leafy salad bowl on a purple plate"></div>
  <div class="abs challenge-top">12 WEEK</div>
  <div class="abs challenge-mid">CHALLENGE</div>
  <div class="abs challenge-tag">HEALTHY, HAPPY &amp; HOT<br>IN <em>NO TIME FLAT!</em></div>
  <div class="abs btn challenge-btn">JOIN US NOW</div>

  <div class="abs join-title">JOIN THE MOVEMENT!</div>
  <div class="abs join-text">Join the Bright Plate Living Movement and get a free copy of <b>The Fresh Start Plan</b> (valued $27.00)!</div>
  <div class="abs field" style="left:558px;top:1052px;width:123px;height:24px">Your Name</div>
  <div class="abs field" style="left:692px;top:1052px;width:123px;height:24px">Your Email</div>
  <div class="abs btn" style="left:558px;top:1089px;width:257px;height:24px;background:var(--purple)">HOOK ME UP</div>
</aside>

<footer>
  <nav class="abs footer-links"><span>COMMUNITY</span><i>/</i><span>FREE RESOURCES</span><i>/</i><span>PRESS</span><i>/</i><span>CONTACT</span></nav>
  <div class="abs copyright">COPYRIGHT © 2013 BRIGHT PLATE LIVING. ALL RIGHTS RESERVED. DISCLAIMER / PRIVACY POLICY</div>
  <div class="abs social" style="left:709px" role="img" aria-label="Chatterbook"></div>
  <div class="abs social" style="left:745px" role="img" aria-label="Chirper"></div>
  <div class="abs social" style="left:781px" role="img" aria-label="ClipTube"></div>
</footer>

</body>
</html>
```